Brackenridge Fish House Menu design

We are a new Seafood Restaurant in NW Montana. We will be the only one in about 200 Miles. We are a Casual/Upscale Restaurant featureing and Oyster Bar/Live Lobster Tank/ Outdoor Seating with beautiful lake views. We have huge garage doors that open up to our big outdoor patio and outdor stage for live music.
I'm interested in having our menu having the ability to add a printed page daily or weekly showing the fresh fish and Oysters that we have as well as specials which will also be represented on the chalk board.
We have 75 Bottle wine list divided by grape variatal such as: Chardonnay, Savagnion Blanc, Reisling, Champagne, Pinot Noir, Melot, Syrah, Cabernet Sauvignon, Interesting Whites and Interesting reds.
We are designing the restaurant to look more Contemporary/urban chic/industrial with reclaimed wood as well. White's Blues and Grey's are the prevolent colors.
I also have a logo we can send over.

Target Market(s)

30-65 age mainly caucasian from the Northwest region as well as tons of Canadians.

Industry/Entity Type

Restaurant

Requirements
Must have
• "Eat the Fish" is our Tagline
American and Canadian flags that are crossed
Family owned and operated

Disclaimer: All steaks and Burgers are cooked to order. "Consuming raw, undercooked and unpasteurized food items may increase your chance of foodborne illnesses." We use nut and nut based oils in some of our menu items. If you are allergic to nuts or any other foods, please let us know.

Also here is the menu: Feel free to use whatever subcatagory heading you choose this was just for us.
FINAL MENU

SMALL PLATES
1. Sweet Thai Chili Calamari
2. Shrimp Stuffed Jalapeños
3. Hamachi Crudo
4. House Smoked Salmon with Tandem Crackers and Pickled Celery
5. Seared Teriyaki Tidbits
6. Sliders
• Crab Salad
• Sausage with Caramelized Onions, Peppers and Provolone
• Mini Cheeseburgers
7. Fried Green Tomatoes with Crab and Tarragon-Chive Aioli
8. Tomato Soup
9. Seafood Bisque
10. House Salad with Choice of Dressings
11. Small Caesar Salad

FARM
1. Caesar Salad Entrees
• Chicken
• Fish
• Crab
2. Seafood Cobb
3. Caprese
4. Farmhouse

SNACKS
1. Fish Tacos
2. Rolls
• Lobster
• Crab
• Shrimp
3. Grilled Chicken Avocado and Bacon
4. Grilled Cheese with Tomato Soup

OCEANS
1. Wood Grilled Black Smoked Sea Salt and Pepper Salmon
2. Miso Black Cod
3. Vela Rino White Fish
4. Whole Fish
5. Fish n Chips
6. Lobster
7. Steamed Clams and/or Mussels
8. Seared Scallops
9. Roasted Garlic Shrimp
10. Crab Cakes with Trio of Dipping Butters

RANCH
1. Wood Grilled 16 oz Rib Eye
2. Wood Grilled 10 oz Top Sirloin
3. Wood Grilled Half Chicken
4. Wood Grilled Pork Chop

SWEETS
1. Key Lime Pie
2. Molted Chocolate Cake
3. Banana Fosters / Cherries Jubilee

Nice to have
• We have a little bit of Hawaiian thing occuring here so you can play around with that or not.

History section would be a nice add as well.
Such as a history section of the Brackenridge itself.

```html
<!DOCTYPE html>
<html lang="en">
<head>
<meta charset="utf-8">
<title>Brackenridge Fish House – Menu System</title>
<link rel="stylesheet" href="https://fonts.googleapis.com/css2?family=Caprasimo&family=Parisienne&family=Tinos&display=swap">
<style>
  :root{
    --ocean:#0b4a8a;
    --ocean-deep:#0a3f77;
    --ocean-shade:#1a5a98;
    --paper:#ffffff;
    --board:#d9d9d9;
    --board-light:#ececec;
    --wood-light:#e6c48e;
    --wood-mid:#d4a866;
    --wood-dark:#c08f4c;
    --burn:#4a2a12;
    --ink:#1b1b1b;
    --shell-light:#efe9df;
    --shell-mid:#cfc2ad;
  }
  *{box-sizing:border-box;margin:0;padding:0}
  html,body{width:1200px;height:860px;overflow:hidden;background:var(--paper)}
  .canvas{position:relative;width:1200px;height:860px}

  .stage{position:absolute;background:radial-gradient(ellipse at center,var(--board-light) 0%,var(--board) 100%)}
  .stage--open{left:20px;top:20px;width:582px;height:320px}
  .stage--closed{left:603px;top:20px;width:582px;height:320px}
  .stage--sections{left:20px;top:350px;width:582px;height:490px}
  .stage--spread{left:603px;top:350px;width:582px;height:490px}

  .stage-label{position:absolute;left:30px;top:10px;font:16px "Tinos",serif;color:var(--ink)}

  .wood{background:linear-gradient(100deg,var(--wood-light) 0%,var(--wood-mid) 35%,var(--wood-light) 55%,var(--wood-dark) 80%,var(--wood-mid) 100%)}

  .brand{font-family:"Caprasimo",serif;font-weight:400;line-height:1.05;text-align:center}
  .tagline{font-family:"Caprasimo",serif;font-weight:400}
  .script{font-family:"Parisienne",cursive}

  /* Outer box open */
  .cover-open{position:absolute;left:120px;top:52px;width:360px;height:250px;display:flex;gap:4px}
  .cover-open__leaf{position:relative;flex:1;border-radius:3px;overflow:hidden}
  .cover-open__leaf svg{position:absolute;inset:0}
  .cover-open__tagline{position:absolute;left:18px;bottom:10px;font-size:18px;color:var(--burn);white-space:nowrap}
  .cover-open__brand{position:absolute;right:8px;bottom:14px;width:62px;font-size:9px;color:var(--burn)}
  .cover-open__page-brand{position:absolute;right:16px;top:20px;width:58px;font-size:8px;color:var(--ocean)}

  /* Outer box closed */
  .cover-closed{position:absolute;left:175px;top:40px;width:232px;height:262px;border-radius:3px}
  .cover-closed__brand{position:absolute;left:40px;top:48px;width:152px;font-size:19px;color:var(--burn)}
  .cover-closed__menu{position:absolute;left:66px;bottom:36px;font-size:24px;line-height:1;color:var(--burn)}
  .cover-closed__tagline{position:absolute;right:14px;bottom:30px;font-size:12px;line-height:1;color:var(--burn);white-space:nowrap}

  /* Section covers */
  .section-cover{position:absolute;width:308px;height:278px;background:var(--paper);box-shadow:0 2px 6px rgba(0,0,0,.25)}
  .section-cover__rule{position:absolute;left:144px;top:0;bottom:0;width:5px;background:var(--ocean)}
  .section-cover__title{position:absolute;left:168px;top:4px;font-size:22px;color:var(--ocean);white-space:nowrap}
  .section-cover--plates{left:20px;top:20px}
  .section-cover--farm{left:40px;top:60px}
  .section-cover--snacks{left:60px;top:100px}
  .section-cover--oceans{left:80px;top:140px}
  .section-cover__shell{position:absolute;left:28px;top:106px;width:92px;height:60px;border-radius:40% 55% 45% 50%;background:radial-gradient(ellipse at 40% 45%,var(--shell-light),var(--shell-mid))}
  .section-cover__brand{position:absolute;left:166px;top:110px;width:118px;font-size:16px;color:var(--ocean)}
  .section-cover__tagline{position:absolute;left:164px;top:196px;width:124px;text-align:center;font-size:17px;color:var(--ocean-deep)}

  /* Inner spread */
  .spread{position:absolute;left:40px;top:120px;width:500px;height:300px;display:flex;box-shadow:0 3px 8px rgba(0,0,0,.3)}
  .spread__flap{position:relative;width:145px;background:var(--paper)}
  .spread__flap .section-cover__shell{left:26px;top:112px;width:88px}
  .spread__panel{position:relative;background:var(--ocean);color:var(--paper)}
  .spread__panel--menu{width:205px;border-right:1px solid var(--ocean-deep)}
  .spread__panel--notes{width:150px;background:linear-gradient(90deg,var(--ocean-deep),var(--ocean))}
  .spread__title{text-align:center;font-size:20px;padding-top:12px}
  .dish-list{list-style:none;margin:22px 10px 0 10px}
  .dish{display:flex;justify-content:space-between;gap:6px;font:8px/1 "Caprasimo",serif;margin-bottom:9px}
  .dish__price{flex:none}
  .disclaimer{margin:66px 10px 0 12px;font:8px/1.55 "Caprasimo",serif;text-align:justify}
  .spread__watermark{position:absolute;left:150px;bottom:6px;font-size:30px;color:var(--ocean-shade);white-space:nowrap;pointer-events:none}
</style>
</head>
<body>
<main class="canvas">

  <section class="stage stage--open">
    <p class="stage-label">Outer Box Open</p>
    <div class="cover-open">
      <div class="cover-open__leaf wood">
        <svg viewBox="0 0 178 250" width="178" height="250" aria-hidden="true">
          <rect x="22" y="14" width="134" height="210" fill="#f4f6f8"/>
          <rect x="62" y="14" width="4" height="150" fill="#0b4a8a"/>
          <path d="M0 120 Q90 96 178 140 L178 250 L0 250 Z" fill="#d4a866"/>
          <path d="M0 120 Q90 96 178 140" fill="none" stroke="#b8823f" stroke-width="2"/>
        </svg>
        <div class="section-cover__shell" role="img" aria-label="Photograph of a nautilus shell" style="left:60px;top:92px;width:56px;height:40px"></div>
        <p class="tagline cover-open__tagline">Eat the Fish</p>
      </div>
      <div class="cover-open__leaf wood">
        <svg viewBox="0 0 178 250" width="178" height="250" aria-hidden="true">
          <path d="M14 10 H170 V200 Q90 190 14 70 Z" fill="#ffffff"/>
          <rect x="70" y="10" width="4" height="190" fill="#0b4a8a"/>
        </svg>
        <p class="brand cover-open__page-brand">Brackenridge Fish House</p>
        <p class="brand cover-open__brand">Brackenridge Fish House</p>
      </div>
    </div>
  </section>

  <section class="stage stage--closed">
    <p class="stage-label">Outer Box Closed</p>
    <div class="cover-closed wood">
      <p class="brand cover-closed__brand">Brackenridge Fish House</p>
      <p class="script cover-closed__menu">Menu</p>
      <p class="tagline cover-closed__tagline">Eat the Fish</p>
    </div>
  </section>

  <section class="stage stage--sections">
    <article class="section-cover section-cover--plates">
      <span class="section-cover__rule"></span>
      <h2 class="script section-cover__title">Small Plates</h2>
    </article>
    <article class="section-cover section-cover--farm">
      <span class="section-cover__rule"></span>
      <h2 class="script section-cover__title">Farm</h2>
    </article>
    <article class="section-cover section-cover--snacks">
      <span class="section-cover__rule"></span>
      <h2 class="script section-cover__title">Snacks</h2>
    </article>
    <article class="section-cover section-cover--oceans">
      <span class="section-cover__rule"></span>
      <h2 class="script section-cover__title">Oceans</h2>
      <div class="section-cover__shell" role="img" aria-label="Photograph of a white spiral seashell"></div>
      <p class="brand section-cover__brand">Brackenridge Fish House</p>
      <p class="tagline section-cover__tagline">Eat the Fish</p>
    </article>
  </section>

  <section class="stage stage--spread">
    <div class="spread">
      <div class="spread__flap">
        <div class="section-cover__shell" role="img" aria-label="Photograph of a white spiral seashell"></div>
      </div>
      <div class="spread__panel spread__panel--menu">
        <h2 class="script spread__title">Oceans</h2>
        <ul class="dish-list">
          <li class="dish"><span>Sea Salt and Pepper Salmon</span><span class="dish__price">220.00</span></li>
          <li class="dish"><span>Miso Black Cod</span><span class="dish__price">00.00</span></li>
          <li class="dish"><span>Vela Rino White Fish</span><span class="dish__price">00000</span></li>
          <li class="dish"><span>Whole Fish</span><span class="dish__price">0000</span></li>
          <li class="dish"><span>Fish n Chips</span><span class="dish__price">000</span></li>
          <li class="dish"><span>Lobster</span><span class="dish__price">0000.00</span></li>
          <li class="dish"><span>Steamed Clams and/or Mussels</span><span class="dish__price">000000</span></li>
          <li class="dish"><span>Seared Scallops</span><span class="dish__price">000</span></li>
          <li class="dish"><span>Roasted Garlic Shrimp</span><span class="dish__price">0000</span></li>
          <li class="dish"><span>Crab Cakes, Trio of Dipping Butters</span><span class="dish__price">0000</span></li>
        </ul>
      </div>
      <div class="spread__panel spread__panel--notes">
        <p class="disclaimer">Disclaimer: All steaks and Burgers are cooked to order. "Consuming raw, undercooked and unpasteurized food items may increase your chance of foodborne illnesses." We use nut and nut based oils in some of our menu items. If you are allergic to nuts or any other foods, please let us know.</p>
      </div>
      <p class="tagline spread__watermark">Eat the Fish</p>
    </div>
  </section>

</main>
</body>
</html>
```